Launching new podcast and need artwork

we are two guys in our early 40's from east Texas who are starting a podcast around personal finance.

The title of the podcast will be "Ledger Gripes" and the subtitle will be "Financial hacks with some southern charm"

We own the company boundlessdaysplanning.example and will be using the podcast as a lead generation for our primary business of financial coaching.

Target Market(s)

Male 35-45 years old

Industry/Entity Type

Personal finance

Requirements
Nice to have
• Rugged or rustic feel would fit our personas

```html
<!DOCTYPE html>
<html lang="en">
<head>
<meta charset="utf-8">
<title>Ledger Gripes — Podcast Cover</title>
<link rel="stylesheet" href="https://fonts.googleapis.com/css2?family=Bebas+Neue&family=Poppins:wght@400;700&display=swap">
<style>
  :root {
    --paper: #ffffff;
    --olive: #4a5726;
    --olive-title: #4a5a27;
    --cash-light: #bdbdb8;
    --cash-mid: #8e8f8a;
    --cash-dark: #6c6d69;
    --glass: #e6e8e2;
    --bronze: #a88a55;
    --bronze-dark: #6b5a36;
    --ink-light: #ffffff;
  }
  html, body {
    margin: 0;
    padding: 0;
    width: 1200px;
    height: 1200px;
    overflow: hidden;
    background: var(--paper);
  }
  .cover {
    position: relative;
    width: 1200px;
    height: 1200px;
    background: var(--paper);
    overflow: hidden;
  }
  .cover__band {
    position: absolute;
    left: 0;
    top: 739px;
    width: 1200px;
    height: 461px;
    background: var(--olive);
  }
  .cover__title {
    position: absolute;
    left: 0;
    top: 0;
    width: 1200px;
    height: 740px;
  }
  .title-word {
    font-family: "Bebas Neue", "Oswald", sans-serif;
  }
  .cover__photo {
    position: absolute;
    left: 764px;
    top: 610px;
    width: 378px;
    height: 540px;
    border-radius: 60px 60px 46px 46px;
    background: linear-gradient(180deg, var(--glass) 0%, #d8d6c8 30%, var(--bronze) 62%, var(--bronze-dark) 100%);
  }
  .cover__tagline {
    position: absolute;
    left: 69px;
    top: 790px;
    margin: 0;
    color: var(--ink-light);
    font-family: "Poppins", sans-serif;
    font-weight: 400;
    font-size: 51px;
    line-height: 53px;
    text-transform: uppercase;
  }
  .cover__tagline strong {
    display: block;
    font-weight: 700;
    font-size: 82px;
    line-height: 80px;
    margin-top: 2px;
  }
  .cover__label {
    position: absolute;
    left: 69px;
    top: 1092px;
    margin: 0;
    color: var(--ink-light);
    font-family: "Poppins", sans-serif;
    font-weight: 400;
    font-size: 28px;
    letter-spacing: 14px;
  }
  .cover__brand {
    position: absolute;
    left: 516px;
    top: 1072px;
    width: 232px;
    margin: 0;
    text-align: center;
    color: var(--ink-light);
    font-family: "Poppins", sans-serif;
    font-weight: 700;
    font-size: 22px;
    line-height: 27px;
    text-transform: uppercase;
  }
</style>
</head>
<body>
  <main class="cover">
    <div class="cover__band"></div>

    <svg class="cover__title" viewBox="0 0 1200 740" aria-label="Ledger Gripes">
      <defs>
        <linearGradient id="cash-fill" x1="0" y1="0" x2="1" y2="1">
          <stop offset="0" stop-color="#8e8f8a"/>
          <stop offset="0.45" stop-color="#bdbdb8"/>
          <stop offset="0.75" stop-color="#9c9d97"/>
          <stop offset="1" stop-color="#6c6d69"/>
        </linearGradient>
      </defs>
      <text class="title-word" x="60" y="403" font-size="462" fill="url(#cash-fill)"
            textLength="1069" lengthAdjust="spacingAndGlyphs">LEDGER</text>
      <text class="title-word" x="66" y="697" font-size="372" fill="#4a5a27"
            textLength="680" lengthAdjust="spacingAndGlyphs">GRIPE$</text>
    </svg>

    <div class="cover__photo" role="img" aria-label="Photo of a glass jar filled with coins with a young green sprout growing out of it"></div>

    <p class="cover__tagline">Financial hacks<br>with some<strong>Southern<br>Charm</strong></p>

    <p class="cover__label">Podcast</p>

    <p class="cover__brand">Boundless Days<br>Planning</p>
  </main>
</body>
</html>
```